Business card for home decor store and design

I need a business card for my home decor boutique that’s professional looking boho/rustic. We sell vintage furniture, vintage finds, lamps, throws, rugs. We also carry a Diy paint line for refinishing furniture. We offer workshop on painting furniture, private or group setting. We in the heart of Old Town Red Bluff. We love to design, build and restore. Family owned small business. Our style is rustic boho farmhouse. We search for one of a kind found and repurposed items. We love vintage home decor, vintage windows.

Target Market(s)

Home decor

Industry/Entity Type

Home Accessories

Contact Information for Business Card

Have a rustic look/boho

Font styles to use
Serif
Script

Requirements
Must have
• Logo

```html
<!DOCTYPE html>
<html lang="en">
<head>
<meta charset="utf-8">
<title>Birch &amp; Loam Co. — Business Card</title>
<link rel="stylesheet" href="https://fonts.googleapis.com/css2?family=Courier+Prime:wght@400;700&family=Kanit:wght@300&display=swap">
<style>
  :root {
    --backdrop: #f2c4b1;
    --card-edge: #f4f3ef;
    --ink: #2a2826;
    --wash-cream: #efe8d2;
    --wash-sand: #e6d3a8;
    --wash-mauve: #b8a0a6;
    --wash-plum: #a08e9c;
    --wash-grey: #cfcbc6;
    --wash-mint: #cfe3d4;
    --wash-ochre: #e4c997;
    --leaf: #9fb58f;
  }
  * { margin: 0; padding: 0; box-sizing: border-box; }
  html, body { width: 1200px; height: 941px; overflow: hidden; }
  body {
    background: var(--backdrop);
    position: relative;
    font-family: "Courier Prime", "Courier New", monospace;
    color: var(--ink);
  }
  .card {
    position: absolute;
    left: 370px;
    width: 460px;
    height: 276px;
    background: var(--card-edge);
    box-shadow: 0 10px 24px rgba(140, 80, 60, 0.18);
    overflow: hidden;
  }
  .card--front { top: 100px; }
  .card--back { top: 535px; }
  .card__wash {
    position: absolute;
    top: 0; bottom: 0; left: 8px; right: 8px;
    background: linear-gradient(90deg,
      var(--wash-cream) 0%, var(--wash-sand) 14%, var(--wash-mauve) 26%,
      var(--wash-plum) 34%, var(--wash-grey) 44%, var(--wash-cream) 58%,
      var(--wash-mint) 72%, var(--wash-cream) 82%, var(--wash-ochre) 94%);
    opacity: 0.85;
  }
  .brand {
    position: absolute;
    display: flex;
    align-items: center;
    gap: 8px;
    font-weight: 700;
    color: var(--ink);
    white-space: nowrap;
  }
  .brand__dot {
    width: 12px; height: 12px;
    border-radius: 50%;
    background: var(--ink);
  }
  .card--front .brand {
    top: 76px; left: 50%;
    transform: translateX(-50%);
    font-size: 22px;
  }
  .tagline {
    position: absolute;
    top: 172px; left: 0; right: 0;
    text-align: center;
    font-size: 16px;
    letter-spacing: 2.2px;
  }
  .services {
    position: absolute;
    top: 212px; left: 0; right: 0;
    text-align: center;
    font-size: 12.5px;
    letter-spacing: 1.6px;
    line-height: 23px;
  }
  .card--back .brand {
    top: 112px; left: 64px;
    font-size: 15px;
  }
  .contact {
    position: absolute;
    right: 58px; top: 150px;
    font-family: "Kanit", Arial, sans-serif;
    font-weight: 300;
    font-size: 15px;
    line-height: 20px;
    text-align: right;
  }
</style>
</head>
<body>
  <section class="card card--front">
    <div class="card__wash" role="img" aria-label="Soft watercolour stripes in cream, mauve, grey and mint with eucalyptus sprigs"></div>
    <div class="brand"><span class="brand__dot"></span>Birch &amp; Loam Co.</div>
    <p class="tagline">WE ARE A FAMILY WHO LOVES</p>
    <p class="services">VINTAGE • DIY • WORKSHOPS • DESIGN<br>• BUILD • RESTORE</p>
  </section>

  <section class="card card--back">
    <div class="card__wash" role="img" aria-label="Soft watercolour stripes in cream, mauve, grey and mint with eucalyptus sprigs"></div>
    <div class="brand"><span class="brand__dot"></span>Birch &amp; Loam Co.</div>
    <p class="contact">Oak Hollow, California<br>+1 555-014-2290<br>@BirchAndLoamCo</p>
  </section>
</body>
</html>
```